TR Advisory Business Cards - High End AV / Low Voltage Company

We are low voltage AV company that specializes in high end clients on the residential side and larger businesses on the commercial side. We want something modern, tech looking but also something that is extremely professional looking. We have uploaded our logos and postcards we already have in the field. Along with a picture of one of our wrapped vans. Our website is at www.trvadvisory.example and our primary colors are the orange, green, grey and blue all military color finishes.

We are interesting in the slogans "Pairing You with the Right Technology" or "Smart Spaces, Clear Signals"

Target Market(s)

We focus on 70% Commercial and 30% Residential Customers

Industry/Entity Type

Low Voltage, AV Company

Contact Information for Business Card

Name - Dorian Fairweather, Title - Owner, Office Phone - 555-714-3096, Mobile Phone - 555-802-4173, E-Mail - d@trvadvisory.example, Website: www.trvadvisory.example

Font styles to use
Sans Serif

Requirements
Must have
• Must have Name, Title, Work Phone & Mobile, Website and Logo.
Nice to have
• We want something that will impress our higher end clients with a great logo
Should not have
• Too traditional or plain.

```html
<!DOCTYPE html>
<html lang="en">
<head>
<meta charset="utf-8">
<title>TR Advisory Business Cards</title>
<link rel="stylesheet" href="https://fonts.googleapis.com/css2?family=Montserrat:wght@400;500;700&display=swap">
<style>
  :root {
    --backdrop: #d3d8d8;
    --card: #eeeeec;
    --orange: #ec6a34;
    --ink: #3b3b3b;
    --ink-soft: #555555;
  }
  * { box-sizing: border-box; margin: 0; padding: 0; }
  html, body {
    width: 1200px; height: 881px; overflow: hidden;
    background: var(--backdrop);
    font-family: "Montserrat", sans-serif;
  }
  .sheet {
    position: relative; width: 1200px; height: 881px;
    display: flex; align-items: center; justify-content: center; gap: 40px;
  }
  .card {
    position: relative; width: 540px; height: 309px;
    background: var(--card);
    border-bottom: 4px solid var(--orange);
    box-shadow: 0 10px 24px rgba(0,0,0,0.18);
  }
  /* logo lockup */
  .brand {
    display: flex; align-items: center; gap: 12px;
    color: var(--orange); font-weight: 700;
    letter-spacing: 0.04em; white-space: nowrap;
  }
  .brand-dot {
    flex: none; border: 3px solid var(--orange); border-radius: 50%;
  }
  /* front */
  .card-front .brand-zone {
    position: absolute; left: 0; top: 0; width: 230px; height: 240px;
    display: flex; align-items: center; justify-content: center;
  }
  .card-front .brand { font-size: 22px; gap: 9px; }
  .card-front .brand-dot { width: 22px; height: 22px; }
  .divider {
    position: absolute; left: 236px; top: 58px; width: 2px; height: 150px;
    background: var(--orange);
  }
  .details { position: absolute; left: 262px; top: 58px; }
  .person-name { color: var(--orange); font-weight: 700; font-size: 25px; line-height: 1.1; white-space: nowrap; }
  .person-title { color: var(--ink-soft); font-size: 14px; margin-top: 4px; }
  .contact-list { list-style: none; margin-top: 18px; }
  .contact-list li {
    display: flex; align-items: center; gap: 9px;
    color: var(--ink); font-size: 13.5px; line-height: 23px; white-space: nowrap;
  }
  .contact-list svg { width: 12px; height: 12px; fill: var(--orange); flex: none; }
  .slogan { color: var(--ink); font-size: 14px; letter-spacing: 0.02em; white-space: nowrap; }
  .card-front .slogan { position: absolute; left: 34px; bottom: 28px; }
  /* back */
  .card-back {
    display: flex; flex-direction: column; align-items: center; justify-content: center; gap: 22px;
  }
  .card-back .brand { font-size: 34px; }
  .card-back .brand-dot { width: 30px; height: 30px; }
</style>
</head>
<body>
<main class="sheet">
  <section class="card card-front">
    <div class="brand-zone">
      <div class="brand"><span class="brand-dot"></span>TR Advisory</div>
    </div>
    <div class="divider"></div>
    <div class="details">
      <h1 class="person-name">Dorian Fairweather</h1>
      <p class="person-title">Owner</p>
      <ul class="contact-list">
        <li><svg viewBox="0 0 12 12"><path d="M1 4c0-2 2-3 5-3s5 1 5 3v1H8V4H4v1H1zM3 6h6l2 5H1z"/></svg>555-714-3096</li>
        <li><svg viewBox="0 0 12 12"><path d="M3 0h6a1 1 0 0 1 1 1v10a1 1 0 0 1-1 1H3a1 1 0 0 1-1-1V1a1 1 0 0 1 1-1zm0 1.5v8h6v-8z"/></svg>555-802-4173</li>
        <li><svg viewBox="0 0 12 12"><path d="M0 2h12v1.2L6 7 0 3.2zM0 4.6l6 3.8 6-3.8V10H0z"/></svg>d@trvadvisory.example</li>
        <li><svg viewBox="0 0 12 12"><circle cx="6" cy="6" r="6"/></svg>www.trvadvisory.example</li>
      </ul>
    </div>
    <p class="slogan">Smart Spaces, Clear Signals</p>
  </section>

  <section class="card card-back">
    <div class="brand"><span class="brand-dot"></span>TR Advisory</div>
    <p class="slogan">Smart Spaces, Clear Signals</p>
  </section>
</main>
</body>
</html>
```